brightleaf7 GROWERS & MAKERS BAZAAR AUTUMN GATHERING FAIR

We need a 4X6 flyer Design for a Farmers Market Harvest Festival. Modern and Fun Design. We sell Local, Organic, and Sustainable Produce and handmade Modern Craft. Designs using Fall Colors. The Design should communicate Autumn, Fall Harvest, Fun, and Modern design. Flyer can be double sided.

Target Market(s)

Moms, 30-55, Foodies

Industry/Entity Type

Festival

Requirements
Must have
• Fall Produce Items, with Modern Design
NOV 10
8-4 @ MARLOW COMMONS
FREE KIDS CRAFT PATCH
PIE EATING CONTEST
PETTING ZOO
FREE FACE PAINTING
BEER TENT
GAMES
LIVE ENTERTAINMENT
CHEF DEMOS
ARTISAN FOOD & CRAFT
LOCAL,ORGANIC,& SUSTAINABLE

WWW.BRIGHTLEAF7.COM
Brightleaf7 Logo
Chef Odalys Logo
Marlow COmmons Logo
Zorvu Logo
BROUGHT TO YOU BY QP DESIGNS
Nice to have
• Ideas for Fall: pumpkins, apples, pears,leaves, Gourds,
Hopefully I can attach our PRevious Fall Harvest Flyers for you to see past designs. Love the Pictaloo Look. Vintage Modern is GOOD!
Should not have
• Country farm look. Country Craft Look

```html
<!DOCTYPE html>
<html lang="en">
<head>
<meta charset="utf-8">
<title>Marlow Commons Harvest Festival Flyer</title>
<link rel="stylesheet" href="https://fonts.googleapis.com/css2?family=Alfa+Slab+One&family=Baloo+2:wght@800&family=Oswald:wght@400;500&family=Rye&display=swap">
<style>
  :root {
    --paper: #e2cab7;
    --plum: #6b3547;
    --sage: #4f5a4c;
    --orange: #ee8a4f;
    --yellow: #f7d24a;
    --cream: #f7efe6;
    --white: #ffffff;
    --pumpkin: #f2a47c;
  }
  html, body {
    margin: 0;
    width: 1200px;
    height: 900px;
    overflow: hidden;
    background: var(--white);
  }
  .flyer {
    position: absolute;
    left: 329px;
    top: 17px;
    width: 576px;
    height: 866px;
    filter: drop-shadow(4px 4px 4px rgba(0,0,0,.45));
  }
  .flyer-bg { fill: var(--paper); }
  .headline { font-family: "Alfa Slab One", serif; }
  .headline--small { fill: var(--sage); font-size: 54px; }
  .headline--large { fill: var(--plum); }
  .event-name { font-family: "Alfa Slab One", serif; fill: var(--white); font-size: 30px; }
  .event-date { font-family: "Rye", serif; fill: var(--plum); font-size: 44px; }
  .rounded { font-family: "Baloo 2", sans-serif; font-weight: 800; }
  .values { fill: var(--orange); }
  .artisan { fill: var(--sage); font-size: 36px; }
  .heart { fill: var(--yellow); stroke: #c9a236; stroke-width: 1.5; }
  .kids-box { fill: var(--sage); }
  .kids-zoo { fill: var(--orange); font-size: 26px; }
  .kids-pie { fill: var(--yellow); font-size: 19px; }
  .kids-patch { fill: var(--white); font-size: 17px; }
  .tag { fill: var(--cream); stroke: #cdb8a6; stroke-width: 1; }
  .tag-hole { fill: var(--paper); }
  .tag-text { font-family: "Oswald", sans-serif; fill: var(--sage); font-weight: 400; }
  .scallop-band { fill: var(--orange); }
  .zigzag-rule { fill: var(--plum); }
  .dash-strip { stroke: var(--cream); stroke-width: 12; stroke-dasharray: 6 4; }
  .sponsor-band { fill: var(--white); }
  .sponsor { font-family: "Oswald", sans-serif; font-weight: 500; fill: var(--sage); }
  .sponsor-credit { font-family: "Oswald", sans-serif; font-weight: 400; fill: var(--sage); font-size: 11px; }
  .sponsor-dot { fill: var(--orange); }
</style>
</head>
<body>
<svg class="flyer" viewBox="0 0 576 866" xmlns="http://www.w3.org/2000/svg">
  <defs>
    <filter id="text-shadow" x="-5%" y="-20%" width="110%" height="150%">
      <feDropShadow dx="2" dy="2" stdDeviation="0" flood-color="#6b3547"/>
    </filter>
  </defs>

  <rect class="flyer-bg" width="576" height="866"/>

  <!-- decorative produce accents -->
  <rect x="376" y="23" width="85" height="70" rx="30" fill="#f5d66a" opacity=".7" role="img" aria-label="Yellow gourd sketch"/>
  <rect x="16" y="153" width="75" height="90" rx="30" fill="#ffffff" opacity=".45" role="img" aria-label="White leaf sketch"/>
  <ellipse cx="268" cy="196" rx="42" ry="22" fill="#e89a70" opacity=".6" role="img" aria-label="Orange leaf sketch"/>

  <!-- headline -->
  <text class="headline headline--small" x="33" y="91" textLength="306" lengthAdjust="spacingAndGlyphs">SUPPORT</text>
  <text class="headline headline--large" x="56" y="208" font-size="130" textLength="485" lengthAdjust="spacingAndGlyphs">MARLOW</text>
  <text class="headline headline--large" x="33" y="298" font-size="98" textLength="508" lengthAdjust="spacingAndGlyphs">COMMONS</text>

  <rect class="scallop-band" x="0" y="318" width="576" height="33" role="img" aria-label="Orange scalloped band with loop pattern"/>

  <!-- event -->
  <text class="event-name" x="29" y="393" textLength="358" lengthAdjust="spacingAndGlyphs" filter="url(#text-shadow)">Farmers Market</text>
  <text class="event-name" x="29" y="438" textLength="358" lengthAdjust="spacingAndGlyphs" filter="url(#text-shadow)">Harvest Festival</text>
  <rect class="zigzag-rule" x="29" y="447" width="358" height="4" role="img" aria-label="Plum zigzag rule"/>

  <text class="event-date" x="401" y="398" textLength="137" lengthAdjust="spacingAndGlyphs">NOV 10</text>
  <text class="event-date" x="401" y="443" textLength="137" lengthAdjust="spacingAndGlyphs">8-4PM</text>

  <!-- values -->
  <text class="rounded values" x="31" y="523" font-size="66" textLength="193" lengthAdjust="spacingAndGlyphs">local</text>
  <text class="rounded values" x="29" y="556" font-size="40" textLength="197" lengthAdjust="spacingAndGlyphs">organic</text>
  <text class="rounded values" x="29" y="588" font-size="30" textLength="197" lengthAdjust="spacingAndGlyphs">sustainable</text>

  <g class="hearts">
    <path class="heart" d="M44 625 L31 610 A7 7 0 0 1 44 601 A7 7 0 0 1 57 610 Z"/>
    <path class="heart" d="M89 625 L76 610 A7 7 0 0 1 89 601 A7 7 0 0 1 102 610 Z"/>
    <path class="heart" d="M128 625 L115 610 A7 7 0 0 1 128 601 A7 7 0 0 1 141 610 Z"/>
    <path class="heart" d="M167 625 L154 610 A7 7 0 0 1 167 601 A7 7 0 0 1 180 610 Z"/>
    <path class="heart" d="M211 625 L198 610 A7 7 0 0 1 211 601 A7 7 0 0 1 224 610 Z"/>
  </g>

  <!-- kids box -->
  <rect class="kids-box" x="26" y="637" width="218" height="76" rx="6"/>
  <text class="rounded kids-zoo" x="37" y="663" textLength="196" lengthAdjust="spacingAndGlyphs">PETTING ZOO</text>
  <text class="rounded kids-pie" x="42" y="683" textLength="184" lengthAdjust="spacingAndGlyphs">pie eating contest</text>
  <text class="rounded kids-patch" x="42" y="703" textLength="184" lengthAdjust="spacingAndGlyphs">free kids craft patch</text>

  <!-- activities tag -->
  <rect x="336" y="668" width="60" height="40" rx="18" fill="#6b3547" opacity=".5" role="img" aria-label="Plum leaf sketch"/>
  <polygon class="tag" points="276,468 346,468 371,518 371,691 251,691 251,518"/>
  <circle class="tag-hole" cx="311" cy="481" r="4"/>
  <text class="tag-text" x="256" y="549" font-size="16" textLength="110" lengthAdjust="spacingAndGlyphs">FREE FACE PAINTING</text>
  <text class="tag-text" x="256" y="576" font-size="30" textLength="110" lengthAdjust="spacingAndGlyphs">BEER TENT</text>
  <text class="tag-text" x="256" y="623" font-size="50" textLength="110" lengthAdjust="spacingAndGlyphs">GAMES</text>
  <text class="tag-text" x="256" y="647" font-size="15" textLength="110" lengthAdjust="spacingAndGlyphs">LIVE ENTERTAINMENT</text>
  <text class="tag-text" x="256" y="675" font-size="26" textLength="110" lengthAdjust="spacingAndGlyphs">CHEF DEMOS</text>

  <!-- artisan -->
  <text class="rounded artisan" x="401" y="488" textLength="140" lengthAdjust="spacingAndGlyphs">artisan</text>
  <circle cx="413" cy="513" r="24" fill="#8a8a86" role="img" aria-label="Engraved apple illustration"/>
  <text class="rounded artisan" x="446" y="531" textLength="95" lengthAdjust="spacingAndGlyphs">food</text>
  <text class="rounded artisan" x="404" y="566" textLength="138" lengthAdjust="spacingAndGlyphs">&amp; craft</text>

  <ellipse cx="467" cy="640" rx="71" ry="56" fill="#f2a47c" role="img" aria-label="Sketched orange pumpkin illustration"/>

  <!-- sponsors -->
  <line class="dash-strip" x1="0" y1="724" x2="576" y2="724"/>
  <rect class="sponsor-band" x="0" y="735" width="576" height="108"/>
  <circle class="sponsor-dot" cx="24" cy="790" r="12" fill="#7ab55c"/>
  <text class="sponsor" x="42" y="800" font-size="24" textLength="100" lengthAdjust="spacingAndGlyphs">brightleaf7</text>
  <text class="sponsor" x="154" y="797" font-size="17" textLength="88" lengthAdjust="spacingAndGlyphs">Chef Odalys</text>
  <text class="sponsor" x="254" y="805" font-size="16" textLength="97" lengthAdjust="spacingAndGlyphs">MARLOW COMMONS</text>
  <text class="sponsor-credit" x="361" y="785" textLength="110" lengthAdjust="spacingAndGlyphs">brought to you by:</text>
  <text class="sponsor" x="361" y="808" font-size="22" textLength="110" lengthAdjust="spacingAndGlyphs">QP DESIGNS</text>
  <text class="sponsor" x="482" y="806" font-size="24" textLength="58" lengthAdjust="spacingAndGlyphs">Zorvu</text>
  <circle class="sponsor-dot" cx="556" cy="790" r="8"/>
</svg>
</body>
</html>
```